business cards for Pollenwick Systems

Require business card design for a technology company supplying systems and networking products to the Data Centre market. Design should be clean and simple, professional and elegant.

the company website is www.pollenwicksystems-demo.com

Target Market(s)

data centres

Industry/Entity Type

Business

Contact Information for Business Card

color scheme is aqua and qhite

Font styles to use
Serif

Colors
85cae6
ffffff

Requirements
Must have
• Business Card design for 2 employees

```html
<!DOCTYPE html>
<html lang="en">
<head>
<meta charset="utf-8">
<title>Pollenwick Systems – Business Card</title>
<link href="https://fonts.googleapis.com/css2?family=Jost:wght@300;400&display=swap" rel="stylesheet">
<style>
  :root {
    --aqua: #85cae6;
    --white: #ffffff;
    --ink: #111111;
    --backdrop: #e4e6e9;
  }
  html, body {
    margin: 0;
    width: 1200px;
    height: 916px;
    overflow: hidden;
    background: var(--backdrop);
    font-family: "Jost", "Futura", sans-serif;
  }
  .card {
    position: absolute;
    left: 383px;
    top: 78px;
    width: 434px;
    height: 760px;
    background: var(--white);
    box-shadow: 0 2px 10px rgba(0,0,0,0.08);
  }
  .card__brand-band {
    height: 380px;
    background: var(--aqua);
    display: flex;
    justify-content: center;
    padding-top: 150px;
    box-sizing: border-box;
  }
  .brand-name {
    margin: 0;
    color: var(--white);
    font-weight: 300;
    font-size: 30px;
    letter-spacing: 0.12em;
    text-transform: uppercase;
    text-align: center;
    line-height: 1.15;
  }
  .card__details {
    position: absolute;
    left: 62px;
    top: 518px;
    color: var(--ink);
  }
  .person-name {
    margin: 0;
    font-size: 22px;
    font-weight: 400;
  }
  .person-role {
    margin: 2px 0 0 -6px;
    font-size: 15px;
    font-weight: 400;
  }
  .contact {
    display: grid;
    grid-template-columns: auto auto;
    margin-top: 26px;
    margin-left: -18px;
    font-size: 17px;
    line-height: 1.35;
  }
  .contact__labels {
    text-align: right;
    padding-right: 5px;
    border-right: 1px solid var(--ink);
  }
  .contact__values {
    padding-left: 5px;
  }
</style>
</head>
<body>
  <article class="card">
    <header class="card__brand-band">
      <h1 class="brand-name">Pollenwick<br>Systems</h1>
    </header>
    <section class="card__details">
      <p class="person-name">Your name</p>
      <p class="person-role">Position</p>
      <div class="contact">
        <div class="contact__labels">T<br>E<br>W</div>
        <div class="contact__values">
          0000 0000 00<br>
          name@pollenwicksystems-demo.com<br>
          www.pollenwicksystems-demo.com
        </div>
      </div>
    </section>
  </article>
</body>
</html>
```